Maple Crest Branding for Contracts and Customer facing documents

We are hoping to create a themed branding for our company. We would like to leverage this across our contracts, documents, and all client information and proposals. www.HomesByMapleCrest.example is our website. We are selling high end custom homes. We am intending to use this template for a Lead Magnet and other marketing.

Target Market(s)

Luxury Custom Home Buyers

Industry/Entity Type

Residential Construction

Other font styles liked:
• You may choose, We want to be elegant but very legible and professional

Colors
0054AA
0677BA
7BADD7
CADEEF
E8F1F8

```html
<!DOCTYPE html>
<html lang="en">
<head>
<meta charset="utf-8">
<title>Maple Crest – New Client Pre-Contract Package</title>
<link href="https://fonts.googleapis.com/css2?family=Montserrat:wght@300;400;600;700;800&family=Great+Vibes&display=swap" rel="stylesheet">
<style>
  :root{
    --navy:#22415c;
    --gold:#d6b46c;
    --teal:#0d5a7a;
    --teal-deep:#0a4f70;
    --ink:#2b2b2b;
    --stripe-beige:#dedbd1;
    --stripe-mist:#e3edf3;
    --white:#ffffff;
    --sky:#7fb2dc;
    --lawn:#5fa83a;
  }
  *{margin:0;padding:0;box-sizing:border-box}
  html,body{width:928px;height:1200px;overflow:hidden;background:var(--white)}
  .page{position:relative;width:928px;height:1200px;overflow:hidden;background:var(--white);
        font-family:"Montserrat",Arial,sans-serif;color:var(--ink);border:1px solid #c9c9c9}
  .page-decor{position:absolute;inset:0;width:100%;height:100%}
  .brand-name{position:absolute;left:612px;top:175px;width:256px;text-align:center;
        font-family:"Montserrat",Arial,sans-serif;font-weight:600;font-size:34px;letter-spacing:1px;color:#222}
  .brand-rule{position:absolute;left:656px;top:273px;width:152px;height:1px;background:#333}
  .address{position:absolute;left:104px;top:322px;font-size:17.5px;font-weight:400;letter-spacing:.6px;color:#333}
  .tagline-box{position:absolute;left:612px;top:305px;width:256px;height:50px;background:var(--navy);
        color:var(--white);font-weight:700;font-size:22px;letter-spacing:1.2px;display:flex;align-items:center;justify-content:center}
  .gold-band{position:absolute;left:0;top:363px;width:868px;height:19px;background:var(--gold)}
  .title-band{position:absolute;left:0;top:382px;width:868px;height:167px;background:var(--navy);overflow:hidden}
  .title-band svg{position:absolute;right:0;top:0}
  .title-accent{position:absolute;left:85px;top:1px;width:6px;height:87px;background:var(--gold)}
  .title{position:absolute;left:125px;top:14px;color:var(--white);font-weight:700;font-size:35px;line-height:43px;letter-spacing:1px}
  .subtitle{position:absolute;left:124px;top:106px;color:var(--white);font-weight:300;font-size:18.5px;line-height:23px;letter-spacing:.8px}
  .hero{position:absolute;left:0;top:549px;width:868px;height:565px;
        background:linear-gradient(180deg,var(--sky) 0%,#b9d4ea 30%,#dfe9ee 48%,#6f9a52 66%,var(--lawn) 78%,#3f8a2a 100%)}
  .credit{position:absolute;left:0;top:1022px;width:868px;display:flex;justify-content:center;align-items:center;gap:26px;
        color:var(--white);font-weight:800;font-size:30px;letter-spacing:.5px;text-shadow:0 2px 3px rgba(0,0,0,.55)}
  .phone{display:flex;align-items:center;gap:8px}
  .phone svg{filter:drop-shadow(0 2px 2px rgba(0,0,0,.5))}
  .website{position:absolute;left:0;top:1066px;width:868px;text-align:center;color:var(--white);
        font-weight:300;font-size:17px;letter-spacing:1.6px;text-shadow:0 1px 2px rgba(0,0,0,.4)}
  .footer-name{position:absolute;left:48px;top:1128px;font-size:15.5px;letter-spacing:1px;font-weight:400;color:#333}
  .page-number{position:absolute;left:858px;top:1128px;font-size:15.5px;color:#333}
</style>
</head>
<body>
<div class="page">
  <svg class="page-decor" viewBox="0 0 1688 2184" preserveAspectRatio="none" aria-hidden="true">
    <defs>
      <linearGradient id="mist" x1="0" y1="0" x2="1" y2="0">
        <stop offset="0" stop-color="#d7e3ea"/>
        <stop offset="1" stop-color="#ffffff"/>
      </linearGradient>
      <linearGradient id="mistFade" x1="0" y1="0" x2="1" y2="1">
        <stop offset="0" stop-color="#edf3f7"/>
        <stop offset="1" stop-color="#ffffff" stop-opacity="0"/>
      </linearGradient>
    </defs>
    <polygon points="0,0 640,0 130,660 0,660" fill="url(#mist)" opacity=".8"/>
    <polygon points="700,0 1220,0 680,660 160,660" fill="url(#mistFade)"/>
    <polygon points="380,0 450,0 300,183 235,183" fill="var(--stripe-beige)"/>
    <polygon points="205,183 225,183 0,505 0,455" fill="var(--stripe-beige)"/>
    <polygon points="660,0 690,0 310,470 287,470" fill="var(--stripe-beige)"/>
    <polygon points="1688,1760 1688,1900 1520,2184 1420,2184" fill="url(#mistFade)"/>
    <polygon points="1688,2000 1688,2060 1630,2184 1590,2184" fill="var(--stripe-mist)"/>
  </svg>

  <div class="brand-name">Maple Crest</div>
  <div class="brand-rule"></div>

  <div class="address">218 Ridgeview Ln., #104 Fairhaven VA, 20100</div>
  <div class="tagline-box">CUSTOM HOMES</div>

  <div class="gold-band"></div>
  <section class="title-band">
    <svg width="240" height="167" viewBox="0 0 240 167" aria-hidden="true">
      <polygon points="0,167 150,22 240,110 240,167 200,167 150,72 45,167" fill="var(--teal)" opacity=".75"/>
      <polygon points="90,167 195,60 240,105 240,167" fill="var(--teal-deep)" opacity=".5"/>
    </svg>
    <div class="title-accent"></div>
    <h1 class="title">NEW CLIENT<br>PRE-CONTRACT PACKAGE</h1>
    <p class="subtitle">INITIAL CONSULTATION &nbsp;•&nbsp; SITE MEETING<br>DRAIN FIELD EXPLORATION &nbsp;•&nbsp; DESIGN PROCESS</p>
  </section>

  <div class="hero" role="img" aria-label="Photograph of a luxury Mediterranean-style custom home with palm trees, a wide green lawn and a pool under a blue sky"></div>

  <div class="credit">
    <span>BY EVAN HARWELL</span>
    <span class="phone">
      <svg width="28" height="28" viewBox="0 0 28 28" aria-hidden="true">
        <circle cx="14" cy="14" r="14" fill="var(--white)"/>
        <path d="M9.5 7.5c.6-.5 1.4-.4 1.8.2l1.6 2.3c.4.6.3 1.3-.2 1.7l-1 .8c.8 1.8 2.2 3.3 4 4.2l.9-1c.5-.5 1.2-.6 1.7-.2l2.3 1.6c.6.4.7 1.3.1 1.8l-1.2 1.2c-.8.8-2 1-3 .6-4-1.6-7-4.7-8.5-8.7-.4-1 0-2.2.8-3z" fill="#222"/>
      </svg>
      555 014 2280
    </span>
  </div>
  <div class="website">WWW.HOMESBYMAPLECREST.EXAMPLE</div>

  <div class="footer-name">MAPLE CREST CUSTOM HOMES</div>
  <div class="page-number">1</div>
</div>
</body>
</html>
```